Book Cover for a book on Quiet Ledgers

I am self-publishing my book on Bookvale and need a book cover made. Below are the details. See attached templates for size we need to use. I also attached a previous cover we had made that I liked. The problem with it was they were two boys helping each other but the book is about women. I'm open to your ideas on the cover though, but I wanted to show you a style I liked as an idea.
Front of Cover
Book Title: Quiet Ledgers
Book Subtitle: Morning Letters of a Harbor Keeper
Author Name: Lorna T. Beckett
Add on the Spine of Cover: Quiet Ledgers and Lorna T. Beckett
Back of the Cover Text:
Quiet Ledgers: Morning Letters of a Harbor Keeper is an honest account of a business owner’s experience attempting to navigate the start-up community while also pursuing spiritual growth. Author Lorna Beckett defines a spiritual entrepreneur as “someone who runs an enterprise with the purpose of growing love rather than material gain.” This book discusses the three dimensions of Quiet Ledgers:
1. The business is an integral part of the founder’s spiritual journey.
2. Employees working for the spiritual enterprise, whether they know it or not, encounter this company because it's part of their spiritual path.
3. The business itself has a life force of its own and its purpose is to further the kingdom of heaven on earth.
These three dimensions happen simultaneously and work together to produce the greatest possible result. However, this can feel confusing to a founder juggling these dimensions while also trying to manage and run a business. This is not a formulaic self-help book or roadmap. Rather, it is a compilation of personal reflections that often seem at odds with the traditional world of entrepreneurship.
Below the description add my picture (see attached for my picture)
Bio text:
Lorna Beckett founded Tellway with the vision of ushering in a life-long education system that shifts away from standardization to one that empowers people to live their purpose. In college, Lorna interned for Bright Lanterns, a women’s empowerment initiative where she recognized her passion for helping people find their voice. Lorna's 20-year journey has come full circle to empowering other female CEOs who are pursuing the path of Quiet Ledgers.
NOTE: Please note that Bookvale puts a bar code on the bottom right of the back cover as is noted on the attached template.
Size template is attached to the brief, here are the sizes typed out:
# Description Width (in) Height (in)
1 Full Cover 12.79 9.25
2 Front Cover 6 9
3 Safe Area 5.875 8.75
4 Bleed 0.125 0.125
5 Margin 0.125 0.125
6 Spine 0.54 9
7 Spine Safe Area 0.415 8.75
8 Spine Margin 0.062 0.062
9 Barcode Margin 0.25 0.25
Pre-publication checklist
BOOKVALE TIPS for the final cover:
1. Save as a PDF. Your cover must be a single PDF that includes the back cover, spine, and front cover as one image.
2. Flatten all transparencies. These can cause the file to print with missing or distorted content. Consult your software's documentation to learn how.
3. Embed your fonts. Consult your software's documentation to learn how.
4. Remove crop marks, color bars, template text. Crop marks are lines showing where pages should be trimmed. Color bars are strips with a series of patches used to ensure color balance during printing. Also, remove any template text, PDF creation guides, or software references.
5. Ensure your cover image meets the minimum resolution of 300 DPI (dots per inch).
6. Optimize PDFs. Optimization is useful to reduce your file size, allowing for higher performance when transferring, uploading, viewing, and printing the files.
7. Remove file security. Locked or encrypted files will fail review.
Target Market(s)
Women who want to be CEOs or are currently CEOs of companies.
Industry/Entity Type
Entrepreneurship, business, spirituality
Requirements
Must have
- Just the text on the description. A very welcoming feel.
Nice to have
- I like the idea of having a sunrise/sunset in the image somehow like in the example I attached to the brief, but again I'm open.
Should not have
- Please don't put any yoga or meditation poses or hands outstretched. I have a lot of interesting ones that look like my example so if you are going to submit after Saturday 10/29, please only do so if you have a new idea! Thanks!

```html
<!DOCTYPE html>
<html lang="en">
<head>
<meta charset="utf-8">
<title>Quiet Ledgers — Full Cover</title>
<link href="https://fonts.googleapis.com/css2?family=Oswald:wght@400;500&family=Marcellus&family=Crimson+Pro:wght@400;600;700&display=swap" rel="stylesheet">
<style>
  :root {
    --ink: #000000;
    --gold: #f5c20f;
    --paper: #ffffff;
    --edge: #3a3a3a;
    --sun-top: #b4471a;
    --sun-mid: #e07a22;
    --sun-glow: #f2a640;
  }
  * { margin: 0; padding: 0; box-sizing: border-box; }
  html, body { width: 1200px; height: 861px; overflow: hidden; background: var(--ink); }
  .cover { position: relative; width: 1200px; height: 861px; background: var(--ink); color: var(--paper); }

  /* ---------- back cover ---------- */
  .back { position: absolute; left: 0; top: 0; width: 574px; height: 861px; }
  .back-title {
    position: absolute; left: 0; top: 40px; width: 574px; text-align: center;
    font-family: "Oswald", sans-serif; font-weight: 400; color: var(--gold);
    font-size: 58px; line-height: 60px; letter-spacing: 1px;
  }
  .blurb {
    position: absolute; left: 72px; top: 168px; width: 433px;
    font-family: "Crimson Pro", serif; font-size: 13.2px; line-height: 16px;
    text-align: justify; color: var(--paper);
  }
  .blurb p { margin-bottom: 16px; }
  .dimensions { list-style: none; margin-bottom: 16px; font-weight: 700; }
  .dimensions li { position: relative; padding-left: 22px; }
  .dimensions li span { position: absolute; left: 0; }
  .author-rule {
    position: absolute; left: 72px; top: 503px; width: 433px;
    display: flex; align-items: center; gap: 18px;
  }
  .author-rule .line { flex: 1; height: 1px; background: var(--gold); }
  .author-rule .name {
    font-family: "Marcellus", serif; font-size: 25px; color: var(--gold); white-space: nowrap;
  }
  .portrait {
    position: absolute; left: 76px; top: 547px; width: 150px; height: 169px;
    background: linear-gradient(160deg, #9fb98a 0%, #7a8f63 45%, #c9455c 100%);
  }
  .bio {
    position: absolute; left: 238px; top: 544px; width: 267px;
    font-family: "Crimson Pro", serif; font-size: 13.2px; line-height: 16px;
    text-align: justify; color: var(--paper);
  }

  /* ---------- spine ---------- */
  .spine {
    position: absolute; left: 574px; top: 0; width: 52px; height: 861px;
    border-left: 1px solid var(--edge); border-right: 1px solid var(--edge);
  }
  .spine-title, .spine-author {
    position: absolute; left: 50%; white-space: nowrap;
    writing-mode: vertical-rl;
    transform: translateX(-50%);
  }
  .spine-title {
    top: 52px; font-family: "Oswald", sans-serif; font-size: 27px;
    letter-spacing: 2px; color: var(--gold);
  }
  .spine-author {
    top: 600px; font-family: "Marcellus", serif; font-size: 25px; color: var(--paper);
    letter-spacing: 1px;
  }

  /* ---------- front cover ---------- */
  .front { position: absolute; left: 626px; top: 0; width: 574px; height: 861px; }
  .sunset {
    position: absolute; left: 0; top: 0; width: 574px; height: 548px;
    background:
      radial-gradient(circle at 545px 210px, #fff6d8 0 42px, #f7c66a 60px, rgba(242,166,64,0) 180px),
      linear-gradient(180deg, var(--sun-top) 0%, var(--sun-mid) 45%, var(--sun-glow) 70%, #5a2a10 92%, var(--ink) 100%);
  }
  .front-title {
    position: absolute; left: 0; top: 486px; width: 574px; text-align: center;
    font-family: "Oswald", sans-serif; font-weight: 400; color: var(--gold);
    font-size: 76px; line-height: 78px; letter-spacing: 1px;
  }
  .subtitle {
    position: absolute; left: 0; top: 656px; width: 574px; text-align: center;
    font-family: "Marcellus", serif; font-size: 26px; color: var(--paper);
  }
  .front-author {
    position: absolute; left: 0; top: 768px; width: 574px; text-align: center;
    font-family: "Marcellus", serif; font-size: 42px; color: var(--paper); letter-spacing: 1px;
  }
</style>
</head>
<body>
<div class="cover">

  <section class="back">
    <h2 class="back-title">QUIET<br>LEDGERS</h2>
    <div class="blurb">
      <p>Quiet Ledgers: Morning Letters of a Harbor Keeper is an honest account of a business owner’s experience attempting to navigate the start-up community while also pursuing spiritual growth. Author Lorna Beckett defines a spiritual entrepreneur as “someone who runs an enterprise with the purpose of growing love rather than material gain.” This book discusses the three dimensions of Quiet Ledgers:</p>
      <ol class="dimensions">
        <li><span>1.</span>The business is an integral part of the founder’s spiritual journey.</li>
        <li><span>2.</span>Employees working for the spiritual enterprise, whether they know it or not, encounter this company because it's part of their spiritual path.</li>
        <li><span>3.</span>The business itself has a life force of its own and its purpose is to further the kingdom of heaven on earth.</li>
      </ol>
      <p>These three dimensions happen simultaneously and work together to produce the greatest possible result. However, this can feel confusing to a founder juggling these dimensions while also trying to manage and run a business. This is not a formulaic self-help book or roadmap. Rather, it is a compilation of personal reflections that often seem at odds with the traditional world of entrepreneurship.</p>
    </div>
    <div class="author-rule">
      <span class="line"></span>
      <span class="name">Lorna T. Beckett</span>
      <span class="line"></span>
    </div>
    <div class="portrait" role="img" aria-label="Author portrait photograph"></div>
    <p class="bio">Lorna Beckett founded Tellway with the vision of ushering in a life-long education system that shifts away from standardization to one that empowers people to live their purpose. In college, Lorna interned for Bright Lanterns, a women’s empowerment initiative where she recognized her passion for helping people find their voice. Lorna's 20-year journey has come full circle to empowering other female CEOs who are pursuing the path of Quiet Ledgers.</p>
  </section>

  <section class="spine">
    <span class="spine-title">QUIET LEDGERS</span>
    <span class="spine-author">Lorna T. Beckett</span>
  </section>

  <section class="front">
    <div class="sunset" role="img" aria-label="Silhouette of two climbers on a cliff against an orange sunset sky"></div>
    <h1 class="front-title">QUIET<br>LEDGERS</h1>
    <p class="subtitle">Morning Letters of a Harbor Keeper</p>
    <p class="front-author">Lorna T. Beckett</p>
  </section>

</div>
</body>
</html>
```